Business Card for Jewelry Business

We need a new namecard design for a jewelry company based in Bangkok, Thailand. We have a new website recently and want the new namecard to reflect our new modern image. I have uploaded our old namecard to show you the information that needs to be on the namecard. Pls check our website www.qelburn.com for the new color scheme to help design the new namecard.

```html
<!DOCTYPE html>
<html lang="en">
<head>
<meta charset="utf-8">
<title>Qelburn Manufacturers – Business Card</title>
<link rel="stylesheet" href="https://fonts.googleapis.com/css2?family=Cinzel:wght@400;500&family=Arimo:wght@400&display=swap">
<style>
  :root {
    --backdrop: #2b2b2d;
    --card-dark: #231f20;
    --silver: #c9c9cc;
    --teal: #52c4c9;
    --white: #ffffff;
    --sand: #e3dbd3;
    --ink: #1c1c1c;
  }
  * { box-sizing: border-box; margin: 0; padding: 0; }
  html, body { width: 1200px; height: 800px; overflow: hidden; background: var(--backdrop); }
  .canvas {
    width: 1200px; height: 800px;
    display: flex; align-items: center; justify-content: center; gap: 40px;
  }
  .card {
    position: relative; width: 540px; height: 309px; overflow: hidden;
    box-shadow: 0 10px 30px rgba(0,0,0,.45);
  }

  /* Back side */
  .card--back { background: var(--card-dark); }
  .brand-mark {
    position: absolute; left: 0; right: 0; top: 112px;
    text-align: center;
    font-family: "Cinzel", serif; font-weight: 400; color: var(--silver);
  }
  .brand-mark__name { display: block; font-size: 38px; letter-spacing: 2px; }
  .brand-mark__sub { display: block; font-size: 10px; letter-spacing: 3px; margin-top: 4px; }
  .social {
    position: absolute; left: 0; right: 0; bottom: 40px;
    display: flex; justify-content: center; gap: 16px;
    font-family: "Arimo", sans-serif; font-size: 12px; color: var(--white);
  }
  .social__item { display: flex; align-items: center; gap: 5px; }
  .social__dot { width: 11px; height: 11px; border-radius: 50%; background: var(--teal); }

  /* Front side */
  .card--front { background: var(--teal); }
  .front-shape { position: absolute; inset: 0; }
  .front-brand {
    position: absolute; right: 40px; top: 108px; text-align: center;
    font-family: "Cinzel", serif; font-weight: 400; color: var(--ink);
  }
  .front-brand__name { display: block; font-size: 26px; letter-spacing: 1px; }
  .front-brand__sub { display: block; font-size: 7px; letter-spacing: 1.5px; margin-top: 2px; }
  .contact {
    position: absolute; left: 34px; top: 56px; color: var(--white);
    font-family: "Arimo", sans-serif;
  }
  .contact__name { font-family: "Cinzel", serif; font-weight: 500; font-size: 20px; letter-spacing: 1px; }
  .contact__title { font-size: 11px; margin-top: 2px; white-space: nowrap; }
  .contact__address { font-size: 11px; line-height: 14px; margin-top: 14px; font-style: normal; }
  .contact__lines { list-style: none; margin-top: 12px; font-size: 11px; line-height: 15px; }
  .contact__lines li { display: flex; align-items: center; gap: 7px; }
  .contact__lines svg { width: 9px; height: 9px; fill: var(--white); flex: none; }
</style>
</head>
<body>
<main class="canvas">

  <section class="card card--back" aria-label="Card back">
    <div class="brand-mark">
      <span class="brand-mark__name">QELBURN</span>
      <span class="brand-mark__sub">MANUFACTURERS</span>
    </div>
    <div class="social">
      <span class="social__item"><span class="social__dot"></span>/Qelburn Manufacturers</span>
      <span class="social__item"><span class="social__dot"></span>@QelburnMfr</span>
    </div>
  </section>

  <section class="card card--front" aria-label="Card front">
    <svg class="front-shape" viewBox="0 0 540 309" preserveAspectRatio="none" aria-hidden="true">
      <path d="M264 0 C256 150 330 272 400 309 L448 309 C350 276 268 160 274 0 Z" fill="var(--sand)"/>
      <path d="M274 0 L540 0 L540 309 L448 309 C350 276 268 160 274 0 Z" fill="var(--white)"/>
    </svg>

    <div class="front-brand">
      <span class="front-brand__name">QELBURN</span>
      <span class="front-brand__sub">MANUFACTURERS</span>
    </div>

    <div class="contact">
      <h1 class="contact__name">NARA SIRIPONG</h1>
      <p class="contact__title">Sales &amp; Product Development Manager</p>
      <address class="contact__address">
        218 Moo 7 Rattanakosin Road<br>
        Trade Processing Zone 5<br>
        Suan Kaew Industrial Estate<br>
        Suan Kaew, Bangkok<br>
        10990 Thailand
      </address>
      <ul class="contact__lines">
        <li><svg viewBox="0 0 10 10"><path d="M2 0.5 L4 2.5 L3 3.7 C3.7 5 5 6.3 6.3 7 L7.5 6 L9.5 8 L8.3 9.5 C4.5 9.2 0.8 5.5 0.5 1.7 Z"/></svg>+662-418-2270-3</li>
        <li><svg viewBox="0 0 10 10"><path d="M2.5 0 H7.5 V10 H2.5 Z M3.4 1 V8 H6.6 V1 Z"/></svg>+662-506-1194</li>
        <li><svg viewBox="0 0 10 10"><path d="M0 2 H10 V8 H0 Z M1 3 L5 5.8 L9 3 V2.8 H1 Z" fill-rule="evenodd"/></svg>hello@qelburn.com</li>
        <li><svg viewBox="0 0 10 10"><circle cx="5" cy="5" r="4.5"/></svg>www.qelburn.com</li>
      </ul>
    </div>
  </section>

</main>
</body>
</html>
```